PSD Only - Wordpress Magazine Theme Design

We need a design for our new Premuim wordpress Magazine theme design based on our basic wire-frame. The theme will be used by people who run online magazine, news website or just blog in general.

The layout of homepage is showing recent posts in many way which is easy to user to customize the section of their homepage to show their post based on various categories.

2 Page design need (Homepage and Single Post)
Updates

Project Deadline Extended
Reason: want to get more designer and I am off for holiday a few days too. Better extend the time for designers as well as me also.

Target Market(s)

General Blogger who want a nice premium theme as well as other content based wesite.

Industry/Entity Type

Online

Font styles to use
Sans Serif

Requirements
Must have
• + Must have 2 page design based on Wireframing. Homepage (home.png) annd Single Post (Single.png)
• + Layout must be based on wireframe.
• + Width 1025px
• + 2 Navigation Menu in Header Must be in different style. When theme goes public, user can choose to have both or only 1 navigation or completely hide both of them.
• + 2 Featured Content Slider as you see in wire-frame. They must be in different style from each other.
• + Those recent news section is only about arrange post in defferent ways which only include post feature image, post title as well as post meta info.
• + Sidebar Widget Must be 300px (not include margin or padding) in order to be able for user to place ads with (300px of width) in sidebar widget)
• + Footer Widget Section should have a bit different colour in order to look different for main layout.
Nice to have
• + Drop down Menu
• + (Optional) Some custom Widget (Based on your imagination and creativity)

```html
<!DOCTYPE html>
<html lang="en">
<head>
<meta charset="utf-8">
<title>DailyPulse Magazine Theme</title>
<link href="https://fonts.googleapis.com/css2?family=Oswald:wght@400;500;700&family=Open+Sans:ital,wght@0,400;0,600;0,700;1,400&display=swap" rel="stylesheet">
<style>
:root{
  --red:#e8391e;
  --red-dark:#c92c14;
  --dark:#262626;
  --darker:#1c1c1c;
  --topbar:#2c2c2c;
  --yellow:#f6d31c;
  --border:#dcdcdc;
  --head-bg:#f3f3f3;
  --text:#222;
  --muted:#888;
  --white:#fff;
}
*{box-sizing:border-box;margin:0;padding:0}
html,body{width:1107px;height:1200px;overflow:hidden;background:var(--white);font-family:"Open Sans",sans-serif;color:var(--text)}
.canvas{position:relative;width:1107px;height:1200px;overflow:hidden}
.abs{position:absolute}

.topbar{left:0;top:0;width:1107px;height:31px;background:var(--topbar)}
.topbar-links{left:42px;top:0;height:31px;display:flex;gap:20px;align-items:center;font:700 10px "Open Sans",sans-serif;color:#ddd;letter-spacing:.2px}
.topbar-search{left:930px;top:0;width:135px;height:31px;border-left:1px solid #555;border-right:1px solid #555;display:flex;justify-content:flex-end;align-items:center;padding-right:12px}

.brand{left:42px;top:84px}
.brand-name{font:700 50px/1 "Oswald",sans-serif;color:var(--red);letter-spacing:-1px}
.brand-tag{font:700 12px "Open Sans",sans-serif;color:var(--darker);margin-top:6px}

.ad-banner{left:363px;top:81px;width:702px;height:87px;background:linear-gradient(90deg,#2a2a2a,#111);display:flex;align-items:center;padding-left:48px}
.ad-copy{flex:1}
.ad-title{font:700 17px "Open Sans",sans-serif;color:var(--white)}
.ad-sub{font:italic 16px "Oswald",sans-serif;color:var(--red);letter-spacing:.5px}
.ad-note{font:14px "Open Sans",sans-serif;color:#aaa}
.ad-button{margin-right:30px;background:var(--red);color:var(--white);font:italic 700 16px "Open Sans",sans-serif;padding:10px 18px;border-radius:3px}

.mainnav{left:42px;top:214px;width:1023px;height:58px;background:var(--dark);display:flex;align-items:center;padding:0 0 0 0}
.mainnav a{font:500 15px "Oswald",sans-serif;color:var(--white);text-decoration:none;padding:0 14px;height:58px;display:flex;align-items:center;letter-spacing:-.2px}
.mainnav a.active{background:var(--red);margin-right:4px;padding:0 14px}
.mainnav a.highlight{color:var(--yellow)}

.ticker{left:42px;top:291px;width:1023px;height:31px;background:var(--red);display:flex;align-items:center;overflow:hidden}
.ticker-label{background:var(--dark);height:31px;display:flex;align-items:center;padding:0 10px;font:500 14px "Oswald",sans-serif;color:var(--white)}
.ticker-items{flex:1;display:flex;gap:40px;padding-left:20px;font:600 11px "Open Sans",sans-serif;color:var(--white);white-space:nowrap;overflow:hidden}
.ticker-nav{background:var(--dark);height:31px;width:60px;display:flex;justify-content:space-around;align-items:center}

.box{border:1px solid var(--border);background:var(--white)}
.box-head{height:38px;background:var(--head-bg);border-bottom:1px solid var(--border);font:500 16px/38px "Oswald",sans-serif;color:#333;padding-left:18px;text-transform:uppercase}
.photo{display:block}

.featured{left:42px;top:363px;width:676px;height:398px}
.featured-img{left:20px;top:20px;width:637px;height:358px;background:radial-gradient(circle at 60% 45%,#e7b79a 0,#c9a27e 25%,#9c9a86 55%,#5d6a66 100%)}
.featured-caption{left:54px;top:307px;background:var(--red);color:var(--white);font:700 19px "Open Sans",sans-serif;padding:8px 10px;letter-spacing:.2px}

.funny{left:42px;top:780px;width:676px;height:460px}
.card{position:absolute;width:308px}
.card-img{width:308px;height:146px}
.card-title{font:500 15px "Oswald",sans-serif;margin-top:22px;text-transform:uppercase}
.card-meta{font:italic 10px "Open Sans",sans-serif;color:var(--muted);margin-top:6px}
.card-excerpt{font:11px/1.55 "Open Sans",sans-serif;color:#555;margin-top:6px}

.side-slider{left:737px;top:363px;width:328px;height:422px}
.side-slider-img{left:20px;top:61px;width:288px;height:347px;background:linear-gradient(180deg,#cfd4d6 0,#9aa0a3 45%,#6c6a5d 75%,#4b3f33 100%)}
.slide-date{left:20px;top:310px;background:var(--red);color:var(--white);font:500 11px "Oswald",sans-serif;padding:3px 8px}
.slide-title{left:20px;top:340px;color:var(--white);font:500 15px "Oswald",sans-serif;text-transform:uppercase}
.slide-dots{left:212px;top:378px;display:flex;gap:6px}
.slide-dots span{width:12px;height:12px;border-radius:50%;border:2px solid #bbb}
.slide-dots span.on{background:#ddd;border-color:#fff}

.video{left:737px;top:814px;width:328px;height:101px}
.video-bar{left:20px;top:57px;width:288px;height:43px;background:var(--dark);display:flex;align-items:center;gap:14px;padding-left:14px;font:600 12px "Open Sans",sans-serif;color:var(--white)}
.video-icon{width:30px;height:22px;background:var(--red);border-radius:4px}

.sparky{left:737px;top:953px;width:328px;height:280px}
.sparky-img{left:20px;top:61px;width:288px;height:140px;background:radial-gradient(circle at 45% 50%,#d9b59a 0,#b9a28a 30%,#8a8b80 65%,#55605d 100%)}
.sparky-title{left:20px;top:216px;font:500 15px "Oswald",sans-serif;text-transform:uppercase}
.sparky-meta{left:20px;top:242px;font:italic 10px "Open Sans",sans-serif;color:var(--muted)}
</style>
</head>
<body>
<div class="canvas">

  <div class="abs topbar"></div>
  <nav class="abs topbar-links"><span>MOST VIEWED ARTICLES</span><span>MOST POPULAR ARTICLES</span></nav>
  <div class="abs topbar-search">
    <svg width="14" height="14" viewBox="0 0 14 14"><circle cx="6" cy="6" r="4.2" fill="none" stroke="#888" stroke-width="2"/><line x1="9" y1="9" x2="13" y2="13" stroke="#888" stroke-width="2"/></svg>
  </div>

  <header class="abs brand">
    <div class="brand-name">DAILYPULSE</div>
    <div class="brand-tag">BRIGHTWIRE NEWS &amp; GOSSIPS</div>
  </header>

  <aside class="abs ad-banner">
    <div class="ad-copy">
      <div class="ad-title">Responsive Ad Unit</div>
      <div class="ad-sub">Voltura Magazine Layout</div>
      <div class="ad-note">Automatic sizing based on the space available</div>
    </div>
    <div class="ad-button">Buy this theme!</div>
  </aside>

  <nav class="abs mainnav">
    <a class="active">HOME</a><a>BLOG STYLE</a><a>ENTERTAINMENT</a><a>LIFESTYLE</a><a>TECH</a><a>TRAVEL</a><a>FASHION</a><a class="highlight">ARCADE DEMO</a>
  </nav>

  <div class="abs ticker">
    <div class="ticker-label">LATEST NEWS:</div>
    <div class="ticker-items">
      <span>Shooting performance of Lumora camera</span>
      <span>How we make choices</span>
      <span>Family Portrait with Peanut Butter</span>
      <span>Selfie on Safari</span>
      <span>Unsuccessful Job Applicant</span>
    </div>
    <div class="ticker-nav">
      <svg width="10" height="12" viewBox="0 0 10 12"><path d="M8 1 3 6l5 5" fill="none" stroke="#fff" stroke-width="2.4"/></svg>
      <svg width="10" height="12" viewBox="0 0 10 12"><path d="M2 1l5 5-5 5" fill="none" stroke="var(--red)" stroke-width="2.4"/></svg>
    </div>
  </div>

  <section class="abs box featured">
    <div class="abs featured-img" role="img" aria-label="Photo of a man in glasses holding a pill bottle and a bottle in a pharmacy"></div>
    <div class="abs featured-caption">HOW CAN I MAKE THE RIGHT CHOICE?</div>
  </section>

  <section class="abs box funny">
    <div class="box-head">Start your day in a funny way</div>
    <article class="card" style="left:19px;top:61px">
      <div class="card-img" role="img" aria-label="Photo of a man in glasses holding a pill bottle" style="background:radial-gradient(circle at 50% 50%,#e0b89a,#a5927c 50%,#5f6864)"></div>
      <h3 class="card-title">How we make choices</h3>
      <div class="card-meta">November 2, 2014, No Comments</div>
      <p class="card-excerpt">I have traced the story back to her. Now she is my only link to finding their secret base. Hey, take care with the plan you have. The plan is strong with this one. I have you....</p>
    </article>
    <article class="card" style="left:347px;top:61px">
      <div class="card-img" role="img" aria-label="Photo of a family posing with a jar of peanut butter" style="background:radial-gradient(circle at 50% 55%,#e8c9a8,#c9b7a0 45%,#e7e4df)"></div>
      <h3 class="card-title">Family portrait with peanut butter</h3>
      <div class="card-meta">November 2, 2014, No Comments</div>
      <p class="card-excerpt">I have traced the story back to her. Now she is my only link to finding their secret base. Hey, take care with the plan you have. The plan is strong with this one. I have you....</p>
    </article>
    <div class="abs" role="img" aria-label="Photo of a man outdoors" style="left:19px;top:370px;width:308px;height:90px;background:linear-gradient(180deg,#b8c0c4,#7c7a6e)"></div>
    <div class="abs" role="img" aria-label="Photo of a man sitting on a truck" style="left:347px;top:370px;width:308px;height:90px;background:linear-gradient(180deg,#d3d6d7,#8e9396)"></div>
  </section>

  <section class="abs box side-slider">
    <div class="box-head">Awesome sidebar slider</div>
    <div class="abs side-slider-img" role="img" aria-label="Photo of a man in a suit sitting on the back of a shuttle truck"></div>
    <div class="abs slide-date">NOVEMBER 2, 2014</div>
    <div class="abs slide-title">Unsuccessful job applicant</div>
    <div class="abs slide-dots"><span></span><span></span><span class="on"></span></div>
  </section>

  <section class="abs box video">
    <div class="box-head">Video of the day</div>
    <div class="abs video-bar"><span class="video-icon"></span>People are awesome and amazing</div>
  </section>

  <section class="abs box sparky">
    <div class="box-head">Today sparky</div>
    <div class="abs sparky-img" role="img" aria-label="Photo of a man in goggles holding a pill bottle"></div>
    <div class="abs sparky-title">Mad professor holds an experiment</div>
    <div class="abs sparky-meta">November 2, 2014, No Comments</div>
  </section>

</div>
</body>
</html>
```